Brochure, website and corporate stationary Design Project

Project scope:
1 x brochure (A4 insert) design
1 x brochure folder design (both external pages and one internal (there will be a few lines of text on the left inside page). The internal right side page will be a pocket for brochures (A4 inserts)
1 x corporate stationary pack (Business Card, logo (a proper logo file format needs to be produced), Letterhead and Envelope)
1 x concept design for our website. You dont need to do the coding. What you need to deliver is the design in a standard format (i.e. photoshop or blend)
Summary: the scope of the project is to design our brochure and its brochure folder, corporate stationary design and graphics concept design for our website. You should also consider our existing logo when performing the above design work (you can modify the logo slightly if you think it would improve look and feel and relevancy to overall design).
• We are a small IT services company
• The folder will be used to hold the brochures (inserts). The folder will be given to prospect customers (see attached a sample service brochure called “VelmaroX User support services Ver0.1.docx”)
• On the cover of the folder, we want to have a design that uses keywords / phrases that reflects our main services (see attached file called “Phrases for presentation folder.docs”). Please note that not all phrases have to be used, use a logic in which ones or add new suggestions
• Inside the folder, at left side we want to have a short text explaining about our services a bit (see attached file called “Brochure Main section v0.91.docx”)
• All designs (corporate stationary, brochure, folder, web, etc.) must be consistent with each other and follow same concept, colour scheme, etc
• you are allowed to do minor changes to our existing logo if you have good reason to do so (see attached logo)
• We want our website design to be simple, elegant, not very colourful, light. HTML5. No flash. (you dont need to do the actual coding of the website, just deliver the design in Photoshop, Blend or any other standard format) With minimal menu items such as: home, services, about us, news, contact us, and other important ones if any. Same colour and design scheme as corporate stationary and brochures
• The company name “VelmaroX” is derived from the Swedish word “Grön” (meaning green) and “roX” which stands for technology but spelled with a “Q” to resemble Quality. The corporate green colour comes from the word “Grön”.
• All templates must be delivered in a standard editable format
Reason: To provide more time to the designers to come with their design submissions.
please note that we more than doubled the budget for this project
Target Market(s)
We deliver IT services to companies of 3-4 employees upto 200-300 employees. The brochures are intended for prospect customers (non IT people)
Industry/Entity Type
Business
Look and feel

```html
<!DOCTYPE html>
<html lang="en">
<head>
<meta charset="utf-8">
<title>Velmarox – About us</title>
<link rel="stylesheet" href="https://fonts.googleapis.com/css2?family=Fira+Sans:wght@400;500&family=Fira+Sans+Condensed:wght@300;400;500&display=swap">
<style>
  :root {
    --backdrop: #dde1e4;
    --paper: #ffffff;
    --panel: #f1f1f1;
    --brand-green: #8cc63f;
    --charcoal: #2e2b2c;
    --ink: #5c5f62;
    --heading: #55585b;
  }
  * { margin: 0; padding: 0; box-sizing: border-box; }
  html, body { width: 1200px; height: 1126px; overflow: hidden; background: var(--backdrop); }
  .sheet {
    position: absolute; left: 202px; top: 0;
    width: 796px; height: 1126px;
    background: var(--panel);
    font-family: "Fira Sans Condensed", "Fira Sans", sans-serif;
    color: var(--ink);
  }
  .masthead {
    position: absolute; left: 0; top: 0; width: 796px; height: 319px;
    background: var(--paper);
  }
  .wordmark {
    position: absolute; left: 38px; top: 124px;
    font-family: "Fira Sans", sans-serif; font-weight: 500;
    font-size: 42px; letter-spacing: 1.5px; color: var(--charcoal);
  }
  .hero-visual {
    position: absolute; right: 0; top: 0; width: 375px; height: 315px;
    background: linear-gradient(135deg, #f6f6f6 0%, #c8d8ae 45%, #a9a9a9 75%, #f4f4f4 100%);
  }
  .accent-rule {
    position: absolute; left: 0; top: 319px; width: 796px; height: 7px;
    background: var(--brand-green);
  }
  .section-title {
    position: absolute; left: 38px; top: 527px;
    font-family: "Fira Sans", sans-serif; font-weight: 400;
    font-size: 25px; color: var(--heading);
  }
  .column { position: absolute; top: 534px; font-size: 11.5px; line-height: 16px; font-weight: 300; }
  .column--intro { left: 211px; width: 270px; }
  .column--services { left: 500px; width: 278px; }
  .column h2 {
    font-size: 11.5px; font-weight: 500; color: var(--brand-green);
    text-transform: uppercase; line-height: 16px;
  }
  .column p { margin-bottom: 16px; }
  .lifecycle .step-arrow { color: var(--brand-green); font-weight: 500; font-size: 13px; }
  .service-list { list-style: none; }
  .service-list li { position: relative; padding-left: 9px; }
  .service-list li::before {
    content: ""; position: absolute; left: 0; top: 6px;
    width: 6px; height: 6px; border-radius: 50%; background: var(--brand-green);
  }
  .footer-band {
    position: absolute; left: 0; top: 1088px; width: 796px; height: 38px;
    background: var(--charcoal);
  }
  .footer-band .footer-tab {
    position: absolute; left: 53px; top: 0; width: 91px; height: 38px;
    background: var(--brand-green);
  }
</style>
</head>
<body>
<main class="sheet">
  <header class="masthead">
    <div class="wordmark">VELMAROX</div>
    <div class="hero-visual" role="img" aria-label="Photograph of glossy grey target spheres around a green bullseye sphere struck by darts"></div>
  </header>
  <div class="accent-rule"></div>

  <h1 class="section-title">About us</h1>

  <section class="column column--intro">
    <h2>Introduction</h2>
    <p>Velmarox is a prominent information technology management consultancy headquartered in Dubai , providing services across the GCC region.</p>
    <p>We work in a unique way by partnering with clients and acting as a trusted advisor for their management team. We provide business leaders with high-quality, up to date and expert strategic advice to help them make informed decisions about their organisations technology investments.</p>
    <p>We cover the entire lifecycle of IT service delivery</p>
    <p class="lifecycle">Management Consultancy <span class="step-arrow">›</span> Solution Design <span class="step-arrow">›</span> Solution Delivery <span class="step-arrow">›</span> Ongoing Supportn</p>
  </section>

  <section class="column column--services">
    <h2>Services</h2>
    <p>Our services include the entire range of technology solutions for small, medium and large businesses.</p>
    <p>We offer strategy and business change advice, systems integration and managed services for infrastructure, applications, cyber security, and development of web and mobile software applications.</p>
    <p>To offer such comprehensive services we have handpicked partners that are the best in their field at what they do be it software development, security audit or data centre setup. This approach allows us to add exceptional quality and depth to our services while eliminating the need for clients to deal with multiple vendors.</p>
    <p>Whether you are a start-up or an established company we have the right range of services for you.<br>These include:</p>
    <ul class="service-list">
      <li>IT Management and Consultancy</li>
      <li>Server, Telephony and Network Installation and Support</li>
      <li>User Support</li>
      <li>Cloud Services – Email, Storage, Business Applications</li>
      <li>Security</li>
      <li>Business Applications (CRM, ERP, Accounting software)</li>
      <li>App Development</li>
    </ul>
  </section>

  <footer class="footer-band"><div class="footer-tab"></div></footer>
</main>
</body>
</html>
```